New Branding Logo and Stationery Design Project

We are looking for a Stationary design for a company called "Peak Renewal". We are a Personal Training business that helps people of diverse ages, fitness levels and goals achieve what they aspire to. We are excellent at what we do and have a high rate of results. We are highly compassionate and love helping people. We want this to show in our logo. The logo must be able to be used on websites but also allow for large printing in the future also.

On the Business Card
Front we need the logo, and underneath this the words "Your health and fitness specialists".
On the back of the card we need:
Name (this will be different on the 2 peoples cards)
Health and fitness specialist
mobile: 04XX-XXX-XXX (we will give to the winner to add)
website: www.peakrenewal-example.com.au
email: info@peakrenewal-example.com.au
Down the bottom of the card we need a section that says something like:
"Your next appointment date is / / time : "

On the letterhead we will need:
Logo
Peak Renewal Pty Ltd
Address
Phone number
Email
Website

Target Market(s)

Anyone, any age who needs help with health and fitness

Industry/Entity Type

Printing

Requirements
Must have
• Templates for business cards here:
https://www.inkmarlow-example.com.au/businesscards_diy.php
Should not have
• Should not be Racist, Sexist, Ageist

```html
<!DOCTYPE html>
<html lang="en">
<head>
<meta charset="utf-8">
<title>Peak Renewal Letterhead</title>
<link href="https://fonts.googleapis.com/css2?family=Quicksand:wght@400;600;700&display=swap" rel="stylesheet">
<style>
  :root {
    --backdrop: #e4e4e4;
    --paper: #f4f4f4;
    --ink: #6b6b6b;
    --ink-soft: #8a8a8a;
    --brand-blue: #3a9fc4;
    --brand-green: #72a93f;
    --watermark: #e6e6e6;
  }
  * { margin: 0; padding: 0; box-sizing: border-box; }
  html, body {
    width: 1200px;
    height: 968px;
    overflow: hidden;
    background: var(--backdrop);
    font-family: "Quicksand", sans-serif;
  }
  .letterhead {
    position: absolute;
    left: 282px;
    top: 34px;
    width: 636px;
    height: 900px;
    background: var(--paper);
    overflow: hidden;
    box-shadow: 0 6px 24px rgba(0,0,0,0.12);
  }
  .brand {
    position: absolute;
    left: 44px;
    top: 44px;
    display: flex;
    align-items: center;
    gap: 12px;
  }
  .brand-name {
    font-size: 26px;
    font-weight: 600;
    letter-spacing: 0.5px;
    color: var(--ink);
    text-transform: uppercase;
    line-height: 1;
  }
  .brand-site {
    display: block;
    margin-top: 5px;
    font-size: 11px;
    font-weight: 400;
    letter-spacing: 0.3px;
    color: var(--ink-soft);
    text-transform: none;
    text-align: right;
  }
  .brand-dot {
    width: 38px;
    height: 38px;
    border-radius: 50%;
    background: var(--brand-blue);
  }
  .contact {
    position: absolute;
    right: 40px;
    top: 128px;
    text-align: right;
    font-size: 9.5px;
    line-height: 1.45;
    color: var(--ink);
  }
  .contact .label-tel { color: var(--brand-blue); font-weight: 700; }
  .contact .label-fax { color: var(--brand-green); font-weight: 700; margin-left: 10px; }
  .watermark {
    position: absolute;
    left: 168px;
    top: 250px;
    width: 300px;
    height: 300px;
    border-radius: 50%;
    background: var(--watermark);
  }
  .footer-wave {
    position: absolute;
    left: 0;
    bottom: 0;
    width: 636px;
    height: 900px;
  }
  .wave-green { fill: var(--brand-green); }
  .wave-blue { fill: var(--brand-blue); }
</style>
</head>
<body>
  <main class="letterhead">
    <header class="brand">
      <div class="brand-name">Peak Renewal
        <span class="brand-site">www.peakrenewal-example.com.au</span>
      </div>
      <div class="brand-dot"></div>
    </header>

    <address class="contact" style="font-style: normal;">
      48 Harbour View Road, Portland<br>
      <span class="label-tel">Tel:</span> 0400-000-123
      <span class="label-fax">Fax:</span> 0400-000-124
    </address>

    <div class="watermark" aria-hidden="true"></div>

    <svg class="footer-wave" viewBox="0 0 636 900" aria-hidden="true">
      <path class="wave-green" d="M0,738 C220,768 460,832 636,872 C460,838 220,784 0,754 Z"/>
      <path class="wave-blue" d="M0,764 C220,794 450,850 636,880 L636,900 L0,900 Z"/>
    </svg>
  </main>
</body>
</html>
```